Cosmetic Clinic Looking For Sign Designs

We are looking for sign design ideas for the front of our building and a lawn sign for our cosmetic injection salon.
I have uploaded the front of our building for a mock up and size, lawn posts with size and a sign that uses the same dimensions.
We would like both signs to be black for the background.

Target Market(s)

Ages 18-75

Industry/Entity Type

Beauty

Requirements
Must have
• Services we offer:
• Cosmetic Injections
• Airbrush Spray Tanning
• Eyelash Growth Serum
• Skin Care Products & More
• Everything must be on a black background
• The lawn sign must have the address: 483 Fenwick and the building sign should have the phone number.
Should not have
• Nothing can light up (no LED)
• Both signs do not need the full address. Just 483 Fenwick and the phone number

```html
<!DOCTYPE html>
<html lang="en">
<head>
<meta charset="utf-8">
<title>Lumera Studio – Lawn Sign</title>
<link href="https://fonts.googleapis.com/css2?family=Roboto+Condensed:wght@400;700&display=swap" rel="stylesheet">
<style>
  :root {
    --sign-black: #000000;
    --sheen-grey: #4a4a4a;
    --band-grey: #4b4b4b;
    --brand-teal: #2398b5;
    --accent-pink: #e5177a;
    --accent-lilac: #7b82bf;
    --text-white: #ffffff;
  }
  * { margin: 0; padding: 0; box-sizing: border-box; }
  html, body {
    width: 821px;
    height: 1200px;
    overflow: hidden;
    background: var(--sign-black);
  }
  .lawn-sign {
    position: relative;
    width: 821px;
    height: 1200px;
    background: var(--sign-black);
    font-family: "Roboto Condensed", "Arial Narrow", sans-serif;
    overflow: hidden;
  }
  .wave-sheen {
    position: absolute;
    inset: 0 0 104px 0;
    background:
      radial-gradient(ellipse 70% 40% at 10% 0%, rgba(90,90,90,0.85), rgba(40,40,40,0.4) 55%, transparent 80%),
      linear-gradient(150deg, transparent 38%, rgba(70,70,70,0.35) 50%, transparent 62%);
  }
  .brand-dot {
    position: absolute;
    left: 336px;
    top: 177px;
    width: 150px;
    height: 150px;
    border-radius: 50%;
    background: var(--accent-lilac);
  }
  .brand-name {
    position: absolute;
    left: 0;
    width: 821px;
    text-align: center;
    color: var(--brand-teal);
    font-weight: 700;
    line-height: 1;
  }
  .brand-name--main {
    top: 412px;
    font-size: 118px;
    letter-spacing: 2px;
  }
  .brand-name--sub {
    top: 530px;
    font-size: 58px;
    letter-spacing: 3px;
  }
  .rule {
    position: absolute;
    top: 557px;
    height: 4px;
    background: var(--accent-pink);
  }
  .rule--left { left: 101px; width: 183px; clip-path: polygon(0 50%, 100% 0, 100% 100%); }
  .rule--right { left: 537px; width: 183px; clip-path: polygon(0 0, 100% 50%, 0 100%); }
  .services {
    position: absolute;
    left: 0;
    top: 0;
    width: 821px;
    list-style: none;
  }
  .service {
    position: absolute;
    left: 0;
    width: 821px;
    text-align: center;
    color: var(--text-white);
    font-size: 47px;
    font-weight: 400;
    line-height: 1;
  }
  .service--1 { top: 689px; }
  .service--2 { top: 780px; }
  .service--3 { top: 869px; }
  .service--4 { top: 958px; }
  .divider {
    position: absolute;
    left: 342px;
    width: 137px;
    height: 8px;
  }
  .divider--lilac { top: 755px; background: var(--accent-lilac); }
  .divider--teal { top: 844px; background: var(--brand-teal); }
  .divider--pink { top: 930px; background: var(--accent-pink); }
  .address-band {
    position: absolute;
    left: 0;
    bottom: 0;
    width: 821px;
    height: 104px;
    background: var(--band-grey);
    display: flex;
    align-items: center;
    justify-content: center;
  }
  .address {
    color: var(--text-white);
    font-weight: 700;
    font-size: 62px;
    line-height: 1;
    letter-spacing: 1px;
  }
</style>
</head>
<body>
  <main class="lawn-sign">
    <div class="wave-sheen" role="img" aria-label="Soft grey flowing line pattern sweeping across the black background"></div>

    <div class="brand-dot"></div>
    <h1 class="brand-name brand-name--main">LUMERA</h1>
    <span class="rule rule--left"></span>
    <p class="brand-name brand-name--sub">STUDIO</p>
    <span class="rule rule--right"></span>

    <ul class="services">
      <li class="service service--1">Cosmetic Injections</li>
      <li class="service service--2">Airbrush Spray Tanning</li>
      <li class="service service--3">Eyelash Growth Serum</li>
      <li class="service service--4">Skin Care Products &amp; More</li>
    </ul>
    <span class="divider divider--lilac"></span>
    <span class="divider divider--teal"></span>
    <span class="divider divider--pink"></span>

    <footer class="address-band">
      <p class="address">483 Fenwick</p>
    </footer>
  </main>
</body>
</html>
```